Car Waterless Cleaner 4 in 1 (100% Natural) Clean, Shine, Protect; Water Repellent. High Eff...

We need to design labels for our Car Care & Cleaning products,
Labels on both 500 ml Bottle Spray sides (text will be provided).
5 and 10 liters Car Shampoo.

I need you to come with Car necessary images (Shining cars, Leather car seats ...)

We are a manufacturer of innovative Green Cleaning products; made with green plants and grain extract, (Leather Cleaner & Conditioner, Multi purpuses Cleaner, Car Shine Polish, car Shampoo)

Target Market(s)

Car Care & Cleaning products, Car Dealer, Car Collectors.

Logo Text

No Idea yet, lol, ;) "Car Tovarex Plume" may be?

Font styles to use
Serif

Requirements
Must have
• Similar projects, Inoovative, Comprehencive, good expertise.

```html
<!DOCTYPE html>
<html lang="en">
<head>
<meta charset="UTF-8">
<title>Waterless Wash &amp; Polish Label</title>
<link href="https://fonts.googleapis.com/css2?family=Montserrat:wght@700;800&family=Oswald:wght@600;700&family=Roboto+Condensed:wght@700&display=swap" rel="stylesheet">
<style>
  :root {
    --label-black: #050505;
    --logo-teal: #2c8f8c;
    --new-red: #e0221b;
    --band-green-dark: #3f5a1c;
    --band-green-light: #8aa24a;
    --title-gold: #e8c24a;
    --title-gold-deep: #b8871c;
    --text-white: #ffffff;
    --badge-cream: #f3f1e4;
    --badge-green: #6a9a2a;
    --sticker-yellow: #f4e03a;
    --car-dark: #15171b;
    --car-light: #3a3f47;
  }
  * { margin: 0; padding: 0; box-sizing: border-box; }
  html, body { width: 880px; height: 1200px; overflow: hidden; background: var(--label-black); }
  .label {
    position: relative;
    width: 880px;
    height: 1200px;
    background: var(--label-black);
    overflow: hidden;
    font-family: "Roboto Condensed", Arial, sans-serif;
    color: var(--text-white);
  }
  .logo-placeholder {
    position: absolute;
    left: 160px;
    top: 95px;
    font-family: "Montserrat", Arial, sans-serif;
    font-weight: 800;
    font-size: 58px;
    line-height: 1.12;
    color: var(--logo-teal);
    letter-spacing: 1px;
  }
  .new-tag {
    position: absolute;
    left: 600px;
    top: 200px;
    width: 190px;
    height: 96px;
    border-radius: 48px;
    background: var(--new-red);
    color: var(--text-white);
    font-family: "Montserrat", Arial, sans-serif;
    font-weight: 800;
    font-size: 44px;
    display: flex;
    align-items: center;
    justify-content: center;
    letter-spacing: 1px;
  }
  .title-band {
    position: absolute;
    left: 0;
    top: 345px;
    width: 880px;
    height: 102px;
    background: linear-gradient(90deg, var(--band-green-dark), var(--band-green-light) 50%, var(--band-green-dark));
    display: flex;
    align-items: center;
    justify-content: center;
  }
  .product-title {
    font-family: "Oswald", Arial, sans-serif;
    font-weight: 700;
    font-size: 62px;
    letter-spacing: 1px;
    background: linear-gradient(180deg, #fff1a8, var(--title-gold) 45%, var(--title-gold-deep));
    -webkit-background-clip: text;
    background-clip: text;
    color: transparent;
  }
  .car-photo {
    position: absolute;
    left: 60px;
    top: 640px;
    width: 820px;
    height: 560px;
    background: radial-gradient(ellipse at 55% 55%, var(--car-light), var(--car-dark) 60%, var(--label-black) 85%);
  }
  .benefits {
    position: absolute;
    left: 130px;
    top: 468px;
    list-style: none;
    font-size: 36px;
    line-height: 1.2;
  }
  .benefits li {
    position: relative;
    padding-left: 38px;
    margin-bottom: 8px;
  }
  .benefits li::before {
    content: "";
    position: absolute;
    left: 0;
    top: 13px;
    border-left: 18px solid var(--text-white);
    border-top: 10px solid transparent;
    border-bottom: 10px solid transparent;
  }
  .natural-badge {
    position: absolute;
    left: 728px;
    top: 478px;
    width: 120px;
    height: 120px;
  }
  .guarantee-sticker {
    position: absolute;
    left: 15px;
    top: 935px;
    width: 190px;
    height: 100px;
    background: var(--sticker-yellow);
    border-radius: 8px;
    color: var(--label-black);
    font-size: 26px;
    line-height: 1.15;
    display: flex;
    align-items: center;
    padding-left: 14px;
  }
  .volume {
    position: absolute;
    left: 720px;
    top: 1100px;
    font-size: 36px;
    color: var(--text-white);
  }
</style>
</head>
<body>
  <main class="label">
    <div class="car-photo" role="img" aria-label="Photo of a glossy black SUV, front three-quarter view"></div>

    <div class="logo-placeholder">YOUR LOGO<br>GOES HERE</div>
    <div class="new-tag">NEW</div>

    <div class="title-band">
      <h1 class="product-title">WATERLESS WASH &amp; PLOISH</h1>
    </div>

    <ul class="benefits">
      <li>Unmistakable showroom shine</li>
      <li>Repels dust and water spots</li>
      <li>No hazy film, swirls, or<br>scratches left behind</li>
    </ul>

    <svg class="natural-badge" viewBox="0 0 120 120" aria-hidden="true">
      <circle cx="60" cy="60" r="58" fill="var(--badge-cream)"/>
      <circle cx="60" cy="60" r="44" fill="none" stroke="var(--badge-green)" stroke-width="3"/>
      <circle cx="60" cy="60" r="18" fill="var(--badge-green)"/>
    </svg>

    <div class="guarantee-sticker">100% Results<br>Guaranteed!</div>
    <div class="volume">500 ml</div>
  </main>
</body>
</html>
```